Dentistry

Dentist's personal business card. No logo needed. The card shoul deliver the massage of reliability, professionalism, experience.
Please ad the full brief of the project: down the line it says: the winning look should be precise and pristine NO pictures of Teeth, smiles, instruments etc.

The details to be desplaid are:
Dr. Rob Valdoni
Doctor of Dental Surgery
PHD
Web. Www.drvaldoni.com
Email. Rob@drvaldoni.com
Tel 07731482590
Surgery address. 27Bharwick road London SW4 7QN UK
82 Fenwyn Row London SW3 2HT. Uk

Reason: Decided to make the payment unrefundable in order to get more designers involved.

Requirements
Should not have
• Logo, teeth, smile any sort of instruments.

```html
<!DOCTYPE html>
<html lang="en">
<head>
<meta charset="utf-8">
<title>Dr. Rob Valdoni – Business Card</title>
<link rel="stylesheet" href="https://fonts.googleapis.com/css2?family=Jost:wght@500;600&family=Open+Sans:wght@400;600&display=swap">
<style>
  :root {
    --brand-blue: #1590e3;
    --card-white: #ffffff;
    --page-bg: #eef1f4;
    --ink-dark: #333a40;
    --card-shadow: 0 10px 30px rgba(20, 40, 70, 0.16);
  }
  * { box-sizing: border-box; margin: 0; padding: 0; }
  html, body { width: 1200px; height: 800px; overflow: hidden; }
  body { background: var(--page-bg); position: relative; }

  .card {
    position: absolute;
    top: 230px;
    width: 540px;
    height: 340px;
    border-radius: 18px;
    overflow: hidden;
    box-shadow: var(--card-shadow);
  }

  /* Front */
  .card--front { left: 40px; background: var(--brand-blue); }
  .name-band {
    position: absolute;
    left: 150px; right: 0;
    top: 108px; height: 104px;
    background: var(--card-white);
    border-radius: 52px 0 0 52px;
    display: flex; flex-direction: column; justify-content: center;
    padding-left: 40px;
    color: var(--brand-blue);
    font-family: "Jost", sans-serif;
    white-space: nowrap;
  }
  .name-band__name { font-size: 26px; font-weight: 600; letter-spacing: 0.8px; line-height: 1.1; }
  .name-band__title { font-size: 17px; font-weight: 600; letter-spacing: 0.5px; margin-top: 4px; padding-left: 34px; }

  /* Back */
  .card--back { left: 620px; background: var(--card-white); }
  .contact-band {
    position: absolute;
    left: 0; top: 88px;
    width: 232px; height: 104px;
    background: var(--brand-blue);
    border-radius: 0 52px 52px 0;
    padding: 16px 0 0 24px;
    color: var(--card-white);
    font-family: "Open Sans", sans-serif;
    font-size: 13px;
  }
  .contact-list { list-style: none; }
  .contact-list li { display: flex; align-items: center; gap: 8px; height: 24px; }
  .contact-list svg { width: 15px; height: 15px; flex: none; }

  .address-list {
    position: absolute;
    left: 262px; top: 162px;
    list-style: none;
    font-family: "Open Sans", sans-serif;
    font-size: 12.5px;
    font-weight: 400;
    color: var(--ink-dark);
    white-space: nowrap;
  }
  .address-list li { display: flex; align-items: center; gap: 6px; height: 22px; }
  .address-list svg { width: 15px; height: 15px; flex: none; }

  .edge-strip {
    position: absolute;
    right: 0; top: 175px;
    width: 24px; height: 96px;
    background: var(--brand-blue);
  }
</style>
</head>
<body>

  <section class="card card--front" aria-label="Card front">
    <div class="name-band">
      <h1 class="name-band__name">DR. ROB VALDONI, PHD</h1>
      <p class="name-band__title">Doctor of Dental Surgery</p>
    </div>
  </section>

  <section class="card card--back" aria-label="Card back">
    <div class="contact-band">
      <ul class="contact-list">
        <li>
          <svg viewBox="0 0 24 24" aria-hidden="true"><path fill="#1c2530" d="M6.6 10.8a15.1 15.1 0 0 0 6.6 6.6l2.2-2.2a1 1 0 0 1 1-.25 11.4 11.4 0 0 0 3.6.57 1 1 0 0 1 1 1V20a1 1 0 0 1-1 1A17 17 0 0 1 3 4a1 1 0 0 1 1-1h3.5a1 1 0 0 1 1 1c0 1.25.2 2.45.57 3.57a1 1 0 0 1-.25 1z"/></svg>
          <span>077 31482590</span>
        </li>
        <li>
          <svg viewBox="0 0 24 24" aria-hidden="true"><rect x="3" y="6" width="18" height="13" rx="1.5" fill="none" stroke="#1c2530" stroke-width="2"/><path d="M3 7l9 7 9-7" fill="none" stroke="#1c2530" stroke-width="2"/></svg>
          <span>Rob@drvaldoni.com</span>
        </li>
        <li>
          <svg viewBox="0 0 24 24" aria-hidden="true"><g fill="none" stroke="#1c2530" stroke-width="1.8"><circle cx="12" cy="12" r="9"/><ellipse cx="12" cy="12" rx="4" ry="9"/><path d="M3 12h18M5 7h14M5 17h14"/></g></svg>
          <span>www.drvaldoni.com</span>
        </li>
      </ul>
    </div>

    <ul class="address-list">
      <li>
        <svg viewBox="0 0 24 24" aria-hidden="true"><path fill="#1590e3" d="M12 3l10 9h-3v9h-5v-6h-4v6H5v-9H2z"/></svg>
        <span>27Bharwick road London SW4 7QN UK</span>
      </li>
      <li>
        <svg viewBox="0 0 24 24" aria-hidden="true"><path fill="#1590e3" d="M12 3l10 9h-3v9h-5v-6h-4v6H5v-9H2z"/></svg>
        <span>82 Fenwyn Row London SW3 2HT. Uk</span>
      </li>
    </ul>

    <div class="edge-strip"></div>
  </section>

</body>
</html>
```